Unique, Impressive, and Modern Business Card

Looking for a distinctive, unique business card. We are distributors of tire repairs supplies, tools, machinery, and chemicals. Our target market are tire repair shops, tire franchises, and mechanic shops. We would like our design to include tire characteristics, and use our business colors. Feel free to use all types design and printing options (emboss, spot uv, foil, etc) QR code may be applied, you can use different size business cards ( standard, square, rounded edge, colored edge, etc), all formats needed for printing, also editable for future changes

Target Market(s)

Automotive, Tire industries

Industry/Entity Type

Tire Industry (automotive)

Contact Information for Business Card

Business logo, business Name (Corvane Supply Inc), Name (Marcus Pellow), Position (President) Address (58 Fernhollow Lane, Brentwood NY 11742), Contact number (Company 1-855-302-4418, Cell 1-631-245-9073, email address (marcus.pellow@corvanesupply.com), URL (www.corvanesupply.com

Requirements
Must have
• Must include Business Colors (Black, Green, Blue, White) see sample website file
Nice to have
• emboss, spot uv, etc

```html
<!DOCTYPE html>
<html lang="en">
<head>
<meta charset="utf-8">
<title>Corvane Supply Inc — Business Card</title>
<link rel="stylesheet" href="https://fonts.googleapis.com/css2?family=Arimo:wght@400;500&display=swap">
<style>
  :root {
    --backdrop: #d9d9d9;
    --card-white: #ffffff;
    --brand-blue: #0617e0;
    --brand-blue-text: #1a1fd6;
    --brand-green: #1fc42a;
    --ink: #111111;
    --gear-dark: #2b2d33;
    --gear-light: #a8acb4;
  }
  * { margin: 0; padding: 0; box-sizing: border-box; }
  html, body { width: 1200px; height: 900px; overflow: hidden; }
  body {
    background: var(--backdrop);
    font-family: "Arimo", Arial, sans-serif;
    color: var(--ink);
    position: relative;
  }
  .card {
    position: absolute;
    top: 257px;
    width: 397px;
    height: 397px;
    border-radius: 28px;
    overflow: hidden;
  }
  .card-front { left: 205px; background: var(--card-white); }
  .card-back { left: 653px; background: var(--brand-blue); }

  .edge-dot {
    position: absolute;
    left: -18px; top: 144px;
    width: 36px; height: 36px;
    border-radius: 50%;
    background: var(--brand-green);
  }
  .brand {
    position: absolute;
    display: flex;
    align-items: center;
    gap: 12px;
  }
  .brand-mark { width: 34px; height: 34px; border-radius: 50%; flex: none; }
  .brand-name { font-size: 26px; font-weight: 400; letter-spacing: 0.5px; white-space: nowrap; }
  .card-front .brand { left: 36px; top: 62px; }
  .card-front .brand-mark { background: var(--brand-blue); }
  .card-front .brand-name { color: var(--ink); }

  .person { position: absolute; left: 36px; top: 143px; }
  .person-name { font-size: 24px; font-weight: 400; line-height: 28px; }
  .person-title { font-size: 18px; color: var(--brand-blue-text); line-height: 20px; }

  .contacts { position: absolute; left: 36px; top: 201px; list-style: none; }
  .contacts li {
    display: flex; align-items: center; gap: 6px;
    font-size: 17px; line-height: 23.5px; white-space: nowrap;
  }
  .contacts svg { width: 17px; height: 17px; flex: none; fill: var(--brand-blue); }

  .address { position: absolute; left: 36px; top: 305px; font-size: 18px; line-height: 23.5px; font-style: normal; }
  .address .company { color: var(--brand-blue-text); }

  .product-photo {
    position: absolute;
    left: 97px; top: 75px;
    width: 200px; height: 145px;
    border-radius: 40px;
    background: radial-gradient(ellipse at 55% 45%, var(--gear-light) 0%, #6b6f78 45%, var(--gear-dark) 100%);
  }
  .card-back .brand { left: 40px; top: 280px; }
  .card-back .brand-mark { background: var(--card-white); width: 40px; height: 40px; }
  .card-back .brand-name { color: var(--card-white); font-size: 28px; }
</style>
</head>
<body>
  <section class="card card-front" aria-label="Business card front">
    <span class="edge-dot"></span>
    <div class="brand">
      <span class="brand-mark"></span>
      <span class="brand-name">CORVANE SUPPLY</span>
    </div>
    <div class="person">
      <p class="person-name">MARCUS PELLOW</p>
      <p class="person-title">President</p>
    </div>
    <ul class="contacts">
      <li><svg viewBox="0 0 24 24"><path d="M6.6 10.8a15 15 0 0 0 6.6 6.6l2.2-2.2c.3-.3.7-.4 1-.2 1.1.4 2.3.6 3.6.6.6 0 1 .4 1 1V20c0 .6-.4 1-1 1A17 17 0 0 1 3 4c0-.6.4-1 1-1h3.5c.6 0 1 .4 1 1 0 1.3.2 2.5.6 3.6.1.3 0 .7-.2 1z"/></svg>1-855-302-4418</li>
      <li><svg viewBox="0 0 24 24"><path d="M7 1h10a2 2 0 0 1 2 2v18a2 2 0 0 1-2 2H7a2 2 0 0 1-2-2V3a2 2 0 0 1 2-2zm0 3v14h10V4zm5 15.5a1 1 0 1 0 0 2 1 1 0 0 0 0-2z"/></svg>1-631-245-9073</li>
      <li><svg viewBox="0 0 24 24"><path d="M2 5h20v14H2zm2 2v.5l8 5 8-5V7zm0 2.8V17h16V9.8l-8 5z"/></svg>marcus.pellow@corvanesupply.com</li>
      <li><svg viewBox="0 0 24 24"><path d="M12 2a10 10 0 1 0 0 20 10 10 0 0 0 0-20zm6.9 6h-3a15 15 0 0 0-1.3-3.9A8 8 0 0 1 18.9 8zM12 4c.8 1.2 1.5 2.5 1.9 4h-3.8c.4-1.5 1.1-2.8 1.9-4zM4.3 14a8 8 0 0 1 0-4h3.4a16 16 0 0 0 0 4zm.8 2h3a15 15 0 0 0 1.3 3.9A8 8 0 0 1 5.1 16zm3-8h-3a8 8 0 0 1 4.3-3.9C8.8 5.3 8.4 6.6 8.1 8zM12 20c-.8-1.2-1.5-2.5-1.9-4h3.8c-.4 1.5-1.1 2.8-1.9 4zm2.3-6H9.7a14 14 0 0 1 0-4h4.6a14 14 0 0 1 0 4zm.3 5.9c.6-1.2 1-2.5 1.3-3.9h3a8 8 0 0 1-4.3 3.9zm1.7-5.9a16 16 0 0 0 0-4h3.4a8 8 0 0 1 0 4z"/></svg>www.corvanesupply.com</li>
    </ul>
    <address class="address">
      <span class="company">Corvane Supply Inc</span><br>
      58 Fernhollow Lane<br>
      Brentwood NY 11742
    </address>
  </section>

  <section class="card card-back" aria-label="Business card back">
    <div class="product-photo" role="img" aria-label="Photo of a steel transmission gear shaft"></div>
    <div class="brand">
      <span class="brand-mark"></span>
      <span class="brand-name">CORVANE SUPPLY</span>
    </div>
  </section>
</body>
</html>
```